Business card design needed

We need a business card for a new business. We are called Little Crew Wearhouse, and we make replica kid size clothing, mainly hi vis shirts, work trousers and shorts. Our long term goal is to include clothing for numerous trades and professions, for our littlest Aussies. We would like a kid friendly card using navy blue, bright orange, bright yellow and bright pink. We haven't set up our web page yet because we want to base it on our final business card design.
Updates

Industry/Entity Type

Clothing

```html
<!DOCTYPE html>
<html lang="en">
<head>
<meta charset="utf-8">
<title>Little Crew Wearhouse – Business Card</title>
<link rel="stylesheet" href="https://fonts.googleapis.com/css2?family=Varela+Round&display=swap">
<style>
  :root {
    --backdrop: #6a3723;
    --navy: #272a66;
    --navy-deep: #1d1f57;
    --navy-glow: #2f3170;
    --gold: #e2b42a;
    --yellow: #f5cc33;
    --yellow-edge: #d9a928;
    --bright-yellow: #f4e52c;
    --block-white: #f4f4f4;
  }
  * { margin: 0; padding: 0; box-sizing: border-box; }
  html, body {
    width: 1200px;
    height: 1181px;
    overflow: hidden;
  }
  body {
    background: var(--backdrop);
    font-family: "Varela Round", sans-serif;
    position: relative;
  }
  .card {
    position: absolute;
    left: 271px;
    width: 658px;
    height: 378px;
    border-radius: 28px;
    overflow: hidden;
    background: radial-gradient(ellipse at 50% 45%, var(--navy-glow) 0%, var(--navy) 45%, var(--navy-deep) 100%);
    box-shadow: 0 8px 14px rgba(0, 0, 0, 0.45);
  }
  .card--front { top: 158px; }
  .card--back { top: 635px; }
  .card__tab {
    position: absolute;
    left: 104px;
    width: 451px;
    height: 13px;
    background: var(--gold);
  }
  .card__tab--top { top: 0; border-radius: 0 0 4px 4px; }
  .card__tab--bottom { bottom: 0; border-radius: 4px 4px 0 0; }

  .brand {
    position: absolute;
    left: 173px;
    top: 162px;
    display: flex;
    align-items: center;
    gap: 12px;
  }
  .brand__square {
    width: 56px;
    height: 56px;
    background: var(--block-white);
  }
  .brand__name {
    color: var(--bright-yellow);
    font-size: 26px;
    white-space: nowrap;
  }

  .band {
    position: absolute;
    left: 0;
    top: 69px;
    width: 100%;
    height: 240px;
    background: radial-gradient(ellipse at 50% 50%, var(--yellow) 0%, var(--yellow) 40%, var(--yellow-edge) 100%);
  }
  .contact {
    position: absolute;
    left: 127px;
    top: 64px;
    color: var(--navy);
  }
  .contact__name { font-size: 25px; line-height: 26px; }
  .contact__role { font-size: 18px; line-height: 22px; margin-bottom: 10px; }
  .contact__line { font-size: 13.5px; line-height: 19px; }
  .band__square {
    position: absolute;
    left: 458px;
    top: 76px;
    width: 96px;
    height: 96px;
    background: var(--block-white);
  }
</style>
</head>
<body>
  <section class="card card--front">
    <div class="card__tab card__tab--top"></div>
    <div class="brand">
      <div class="brand__square"></div>
      <span class="brand__name">Little Crew Wearhouse</span>
    </div>
    <div class="card__tab card__tab--bottom"></div>
  </section>

  <section class="card card--back">
    <div class="card__tab card__tab--top"></div>
    <div class="band">
      <div class="contact">
        <p class="contact__name">Your Name</p>
        <p class="contact__role">Business Position</p>
        <p class="contact__line">yourname@email.com</p>
        <p class="contact__line">Phone 0123-456-7890</p>
        <p class="contact__line">www.yourwebsite.com</p>
      </div>
      <div class="band__square"></div>
    </div>
    <div class="card__tab card__tab--bottom"></div>
  </section>
</body>
</html>
```